Awards Banquet Invitation

The Cedar Bluff Area Chamber of Commerce is celebrating it's 65th year at our Annual Awards Banquet (business leader awards). Since we were founded in 1950, we will have a 1950's theme. Dress will be 1950's Formal. I don't want cheesy 1950's. I want Classic feel and fonts from that era. This event is for business professionals so looks from ads in the 50's would be good for inspiration. I would like a look that I can use for the program and event ads. Invitation will include an RSVP insert. Date: February 10, 2015. Time: 6 cocktails, 7 dinner & program, Location: Holm Weide Country Club. Dress is 1950's formal

Target Market(s)

Business owners - our members

Industry/Entity Type

Business

Other font styles liked:
• Lasalle, linotype, thirsty

Colors
86cfc6
474747
ffffff
000000

Requirements
Must have
• classic 50's font and old-fashioned feel
Should not have
• sock hop, soda fountain, 50's diner

```html
<!DOCTYPE html>
<html lang="en">
<head>
<meta charset="utf-8">
<title>Annual Awards Banquet Invitation</title>
<link rel="stylesheet" href="https://fonts.googleapis.com/css2?family=Lobster+Two&family=Libre+Baskerville:wght@400;700&display=swap">
<style>
  :root {
    --teal: #55bfd1;
    --teal-soft: #86cfc6;
    --slate: #36555a;
    --ink: #000000;
    --charcoal: #474747;
    --paper: #ffffff;
    --stage: #ececec;
  }
  * { margin: 0; padding: 0; box-sizing: border-box; }
  html, body {
    width: 1200px;
    height: 1000px;
    overflow: hidden;
    background: var(--stage);
  }
  .invitation {
    position: absolute;
    left: 300px;
    top: 75px;
    width: 600px;
    height: 850px;
    overflow: hidden;
    box-shadow: 0 6px 24px rgba(0,0,0,0.18);
  }
  .invitation__pattern {
    position: absolute;
    inset: 0;
    background:
      radial-gradient(circle at 25% 30%, var(--teal) 0%, var(--slate) 70%),
      var(--slate);
    background-blend-mode: normal;
  }
  .invitation__shapes {
    position: absolute;
    inset: 0;
  }
  .text-block {
    position: absolute;
    left: 0;
    width: 100%;
    text-align: center;
  }
  .event-date {
    top: 52px;
    font-family: "Lobster Two", cursive;
    font-size: 24px;
    color: var(--teal);
  }
  .event-venue {
    top: 86px;
    font-family: "Libre Baskerville", serif;
    font-size: 16px;
    color: var(--paper);
  }
  .invite-lead {
    top: 305px;
    font-family: "Libre Baskerville", serif;
    font-size: 21px;
    color: var(--ink);
  }
  .invite-anniversary {
    top: 332px;
    font-family: "Lobster Two", cursive;
    font-size: 50px;
    color: var(--teal);
  }
  .invite-joiner {
    top: 398px;
    font-family: "Libre Baskerville", serif;
    font-size: 12px;
    color: var(--ink);
  }
  .invite-banquet {
    top: 410px;
    font-family: "Lobster Two", cursive;
    font-size: 34px;
    color: var(--ink);
  }
  .invite-by {
    top: 460px;
    left: 130px;
    width: 340px;
    display: flex;
    align-items: center;
    gap: 12px;
    font-family: "Libre Baskerville", serif;
    font-size: 13px;
    color: var(--ink);
  }
  .invite-by::before,
  .invite-by::after {
    content: "";
    flex: 1;
    height: 1px;
    background: var(--teal);
  }
  .invite-host {
    top: 487px;
    font-family: "Libre Baskerville", serif;
    font-size: 14px;
    color: var(--ink);
  }
  .event-time {
    top: 745px;
    font-family: "Libre Baskerville", serif;
    font-size: 16px;
    color: var(--paper);
  }
  .event-dress {
    top: 781px;
    display: flex;
    justify-content: center;
    align-items: center;
    gap: 10px;
    font-family: "Libre Baskerville", serif;
    font-weight: 700;
    font-size: 16px;
    color: var(--paper);
  }
  .event-dress__mark {
    width: 22px;
    height: 14px;
  }
</style>
</head>
<body>
  <main class="invitation">
    <div class="invitation__pattern" role="img" aria-label="Teal and slate geometric pinwheel pattern"></div>

    <svg class="invitation__shapes" viewBox="0 0 600 850" width="600" height="850" aria-hidden="false">
      <defs>
        <linearGradient id="panel-fill" x1="0" y1="0" x2="1" y2="1">
          <stop offset="0" stop-color="#f6f7fa"/>
          <stop offset="0.5" stop-color="#ffffff"/>
          <stop offset="1" stop-color="#eceef2"/>
        </linearGradient>
      </defs>
      <polygon class="band-top" points="0,0 600,0 300,160" fill="#000000"/>
      <polygon class="band-bottom" points="300,610 600,850 0,850" fill="#000000"/>
      <polygon class="panel-border" points="300,168 565,388 300,608 35,388"
               fill="#86cfc6" stroke="#86cfc6" stroke-width="22" stroke-linejoin="round"/>
      <polygon class="panel" points="300,180 550,388 300,596 50,388"
               fill="url(#panel-fill)" stroke="url(#panel-fill)" stroke-width="18" stroke-linejoin="round"
               role="img" aria-label="Soft white circle pattern behind the invitation text"/>
    </svg>

    <p class="text-block event-date">February 10, 2015</p>
    <p class="text-block event-venue">Holm Weide Country Club</p>

    <p class="text-block invite-lead">You’re Invited to our</p>
    <h1 class="text-block invite-anniversary" style="font-weight:400">65th Anniversary</h1>
    <p class="text-block invite-joiner">at the</p>
    <h2 class="text-block invite-banquet" style="font-weight:400">Annual Awards Banquet</h2>
    <p class="text-block invite-by">by</p>
    <p class="text-block invite-host">Cedar Bluff Area Chamber of Commerce</p>

    <p class="text-block event-time">6 cocktails, 7 dinner &amp; program</p>
    <p class="text-block event-dress">
      <span>Dress code</span>
      <svg class="event-dress__mark" viewBox="0 0 22 14" aria-hidden="true">
        <polygon points="11,0 22,7 11,14 0,7" fill="#55bfd1"/>
      </svg>
      <span>1950’s formal</span>
    </p>
  </main>
</body>
</html>
```